Baby Care Print Log for Nannies and Parents- Creating a brand/style I can use across different forms

I am creating a notebook for babysitters to use to communicate with parents about the children they care for. I will be creating many different forms (emergency contacts, daily logs, shopping lists, etc.)
I need a look and feel from which to style these forms from. I am starting by designing the daily baby care log. I need a designer to take my Word doc with just text on it, and create a visual approach to make this visually appealing.
I do not want this to be extremely "babyish" with cartoon styling. I want it to be more of a professional looking style. I would like to be able to color each different document a different color palette, yet keep the similar look and feel. My logo is attached for inspiration. I use real photography across my website velmorapath.com.
Updates
I will be re-designing my Wordpress website based on what design I like best and also will need other forms completed once I pick a design. I am hoping to work with someone who I can hire for further development needs as well. Added Saturday, February 11, 2017
Target Market(s)
Professional Parents
Industry/Entity Type
Education
Requirements
Must have
- color, pop, visual appeal
- Please use the color in my logo and any complementary colors that you think work well with it. I definitely like colored patterns, ombre, colored backgrounds, etc. I'd prefer for it not to be completely white with only pops of color here and there.
Nice to have
- My logo somewhere subtly on the form
- Photography elements
Should not have
- cartoon images of babies, etc. I use real photography across my website with the exception of my logo umbrella.

```html
<!DOCTYPE html>
<html lang="en">
<head>
<meta charset="utf-8">
<title>Daily Baby Care Log</title>
<link rel="stylesheet" href="https://fonts.googleapis.com/css2?family=Nunito:wght@600;700;800&family=Open+Sans:wght@400;600&display=swap">
<style>
:root{
  --page:#ffffff;
  --band:#4fbccb;
  --title-dark:#176f70;
  --title-light:#3aa7b5;
  --ink:#222222;
  --rule:#9a9a9a;
  --frame:#a8a8a8;
  --nap-light:#d8b2ff;
  --nap-dark:#9b5fd6;
  --nap-text:#5a2c8a;
  --feed-light:#ffcf9e;
  --feed-dark:#f0974a;
  --feed-text:#b45a12;
  --diaper-light:#a9ec76;
  --diaper-dark:#7fd845;
  --diaper-text:#2f6d12;
  --supply:#4daba6;
  --notes:#e94d8e;
  --box-green:#8ccc5c;
  --dot:#4fbccb;
}
*{box-sizing:border-box;margin:0;padding:0}
html,body{width:996px;height:1200px;overflow:hidden;background:var(--page)}
body{position:relative;font-family:"Open Sans",Arial,sans-serif;color:var(--ink)}
.top-band{position:absolute;left:0;top:0;width:996px;height:22px;background:var(--band)}
.title{position:absolute;left:60px;top:50px;font-family:"Nunito",sans-serif;line-height:1}
.title-small{font-size:32px;font-weight:700;color:var(--title-dark)}
.title-big{font-size:44px;font-weight:800;color:var(--title-dark)}
.title-sub{display:block;margin-top:8px;font-size:31px;font-weight:700;color:var(--title-light);letter-spacing:1px}
.brand{position:absolute;left:700px;top:62px;display:flex;align-items:center;gap:12px;font-family:"Nunito",sans-serif;font-size:34px;font-weight:700;color:var(--ink)}
.brand-dot{width:26px;height:26px;border-radius:50%;background:var(--band)}
.name-row{position:absolute;left:39px;top:160px;width:886px;height:28px;border-bottom:1.5px solid var(--rule);font-size:17px}
.name-row .date{position:absolute;left:744px}
.card{position:absolute;border:1.5px dashed var(--frame);border-radius:12px;overflow:hidden;background:var(--page)}
.card-head{height:41px;display:flex;align-items:center;justify-content:center;font-family:"Nunito",sans-serif;font-size:21px;font-weight:700;letter-spacing:2px}
.card-cols{height:23px;display:flex;color:#fff;font-size:14px;align-items:center}
.card-cols span{text-align:center}
.rule{position:absolute;height:1.5px;background:var(--rule)}
.nap{left:72px;top:218px;width:382px;height:304px}
.nap .card-head{background:var(--nap-light);color:var(--nap-text)}
.nap .card-cols{background:var(--nap-dark)}
.feed{left:515px;top:218px;width:382px;height:304px}
.feed .card-head{background:var(--feed-light);color:var(--feed-text)}
.feed .card-cols{background:var(--feed-dark)}
.two-col span{width:50%}
.diapers{left:75px;top:554px;width:345px;height:335px}
.diapers .card-head{height:44px;background:var(--diaper-light);color:var(--diaper-text)}
.diapers .card-cols{height:20px;background:var(--diaper-dark)}
.check{position:absolute;width:25px;height:25px;border:2px solid var(--box-green);border-radius:2px}
.supplies{left:531px;top:554px;width:349px;height:332px}
.supplies .card-head{height:47px;background:var(--supply);color:#fff;font-size:22px}
.supply-item{position:absolute;display:flex;align-items:center;gap:10px;font-size:15px}
.supply-item::before{content:"";width:10px;height:10px;border:2px solid var(--dot);border-radius:50%}
.notes{left:31px;top:926px;width:930px;height:236px}
.notes .card-head{height:41px;justify-content:flex-start;padding-left:22px;background:var(--notes);color:#fff;font-size:22px}
.art{position:absolute}
.art-pacifier{left:462px;top:489px;width:60px;height:72px;border-radius:50%;background:radial-gradient(circle,#f7d9a6,#b9cfe2)}
.art-bottle{left:880px;top:437px;width:60px;height:102px;border-radius:18px;background:linear-gradient(#f3c77d 0 20%,#dbeefb 20%)}
.art-blocks{left:482px;top:802px;width:118px;height:109px;border-radius:10px;background:linear-gradient(135deg,#f4e3a3,#bfe3a5,#b7d3ea)}
.art-duck{left:0;top:1105px;width:106px;height:95px;border-radius:50% 50% 10px 40%;background:linear-gradient(#ffe98a,#f7d04a)}
</style>
</head>
<body>
<div class="top-band"></div>

<h1 class="title"><span class="title-small">your </span><span class="title-big">daily baby’s</span><span class="title-sub">CARE LOG</span></h1>

<div class="brand"><span class="brand-dot"></span>Velmora Path</div>

<div class="name-row"><span>NAME:</span><span class="date">DATE:</span></div>

<section class="card nap">
  <div class="card-head">NAP TIME</div>
  <div class="card-cols two-col"><span>Time</span><span>How Long</span></div>
  <div class="rule" style="left:12px;top:98px;width:192px"></div><div class="rule" style="left:226px;top:98px;width:144px"></div>
  <div class="rule" style="left:12px;top:142px;width:192px"></div><div class="rule" style="left:226px;top:142px;width:144px"></div>
  <div class="rule" style="left:12px;top:185px;width:192px"></div><div class="rule" style="left:226px;top:185px;width:144px"></div>
  <div class="rule" style="left:12px;top:229px;width:192px"></div><div class="rule" style="left:226px;top:229px;width:144px"></div>
  <div class="rule" style="left:12px;top:268px;width:192px"></div><div class="rule" style="left:226px;top:268px;width:144px"></div>
</section>

<section class="card feed">
  <div class="card-head">FEEDING</div>
  <div class="card-cols two-col"><span>Time</span><span>What</span></div>
  <div class="rule" style="left:12px;top:98px;width:192px"></div><div class="rule" style="left:226px;top:98px;width:144px"></div>
  <div class="rule" style="left:12px;top:142px;width:192px"></div><div class="rule" style="left:226px;top:142px;width:144px"></div>
  <div class="rule" style="left:12px;top:185px;width:192px"></div><div class="rule" style="left:226px;top:185px;width:144px"></div>
  <div class="rule" style="left:12px;top:229px;width:192px"></div><div class="rule" style="left:226px;top:229px;width:144px"></div>
  <div class="rule" style="left:12px;top:268px;width:192px"></div><div class="rule" style="left:226px;top:268px;width:144px"></div>
</section>

<section class="card diapers">
  <div class="card-head">DIAPERS</div>
  <div class="card-cols"><span style="width:190px">Time</span><span style="width:70px">Wet</span><span style="width:60px">BM</span></div>
  <div class="rule" style="left:10px;top:116px;width:173px"></div><div class="check" style="left:218px;top:94px"></div><div class="check" style="left:284px;top:94px"></div>
  <div class="rule" style="left:10px;top:157px;width:173px"></div><div class="check" style="left:218px;top:135px"></div><div class="check" style="left:284px;top:135px"></div>
  <div class="rule" style="left:10px;top:196px;width:173px"></div><div class="check" style="left:218px;top:174px"></div><div class="check" style="left:284px;top:174px"></div>
  <div class="rule" style="left:10px;top:236px;width:173px"></div><div class="check" style="left:218px;top:214px"></div><div class="check" style="left:284px;top:214px"></div>
  <div class="rule" style="left:10px;top:276px;width:173px"></div><div class="check" style="left:218px;top:254px"></div><div class="check" style="left:284px;top:254px"></div>
  <div class="rule" style="left:10px;top:315px;width:173px"></div><div class="check" style="left:218px;top:293px"></div><div class="check" style="left:284px;top:293px"></div>
</section>

<section class="card supplies">
  <div class="card-head">SUPPLIES NEEDED SOON</div>
  <div class="supply-item" style="left:26px;top:69px">Diapers</div>
  <div class="supply-item" style="left:203px;top:69px">Baby Food</div>
  <div class="supply-item" style="left:26px;top:107px">Diaper Cream</div>
  <div class="supply-item" style="left:203px;top:107px">Cereal</div>
  <div class="supply-item" style="left:26px;top:143px">Milk/Formula</div>
  <div class="supply-item" style="left:203px;top:143px">Wet Wipes</div>
  <div class="supply-item" style="left:26px;top:180px">Other:</div>
</section>

<section class="card notes">
  <div class="card-head">SPECIAL NOTES</div>
  <div class="rule" style="left:78px;top:79px;width:828px"></div>
  <div class="rule" style="left:78px;top:118px;width:828px"></div>
  <div class="rule" style="left:78px;top:156px;width:828px"></div>
  <div class="rule" style="left:78px;top:196px;width:828px"></div>
</section>

<div class="art art-pacifier" role="img" aria-label="Illustration of a baby pacifier"></div>
<div class="art art-bottle" role="img" aria-label="Illustration of a baby bottle"></div>
<div class="art art-blocks" role="img" aria-label="Illustration of stacked alphabet toy blocks"></div>
<div class="art art-duck" role="img" aria-label="Illustration of a yellow rubber duck"></div>
</body>
</html>
```